Tradelo Size Charts - 6 Products

Hi Koby,

I had you in mind for this, but we have a new e-commerce store that requires the attached 6 size charts re-designed. They are terrible charts from drop shippers and we need them re-designed to match the Talvoro brand logo to designed.

Chart needs to be white background and black letter's. You can add some smart gradients or design to it if you want to make it look elegant and confident.

Can you design 1 chart and we can amend it to perfection with feedback?
Once we agree on the style - you can then do the same style and design for the remaining charts.

Let me know if this is ok?

```html
<!DOCTYPE html>
<html lang="en">
<head>
<meta charset="utf-8">
<title>Size Chart</title>
<link href="https://fonts.googleapis.com/css2?family=Poppins:wght@700;800&family=Open+Sans:wght@400;600&display=swap" rel="stylesheet">
<style>
  :root{
    --bg-top:#dbfcf3;
    --bg-bottom:#f6fffd;
    --ink:#1f1f1f;
    --text:#2b2b2b;
    --rule:#111111;
    --grid:#a9a9a9;
    --size-pink:#f0185a;
    --bust-purple:#a51adb;
    --waist-amber:#ec9c10;
    --length-blue:#33aed8;
    --white:#ffffff;
  }
  *{margin:0;padding:0;box-sizing:border-box}
  html,body{width:1200px;height:1012px;overflow:hidden}
  body{
    position:relative;
    background:linear-gradient(180deg,var(--bg-top) 0%,var(--bg-bottom) 100%);
    font-family:"Open Sans",Arial,sans-serif;
    color:var(--text);
  }
  .title-rule{position:absolute;top:73px;height:4px;background:var(--rule)}
  .title-rule.left{left:70px;width:329px}
  .title-rule.right{left:825px;width:328px}
  .chart-title{
    position:absolute;left:0;width:1240px;top:28px;text-align:center;
    font-family:"Poppins",Arial,sans-serif;font-weight:800;font-size:66px;
    line-height:80px;color:var(--ink);letter-spacing:0.5px;
  }
  .chart-unit{
    position:absolute;left:0;width:1240px;top:101px;text-align:center;
    font-size:24px;line-height:30px;color:var(--ink);
  }
  .size-table{
    position:absolute;left:98px;top:183px;width:1020px;height:556px;
    background:var(--white);border:1px solid var(--grid);
    display:grid;
    grid-template-columns:256px 255px 254px 255px;
    grid-template-rows:101px 94px 89px 91px 90px 91px;
  }
  .cell{
    display:flex;align-items:center;justify-content:center;
    border-top:1px solid var(--grid);
    font-size:21px;color:var(--ink);
  }
  .cell + .cell{border-left:1px solid var(--grid)}
  .header-cell{border-top:none}
  .row-first .cell{border-top:none}
  .row-first{display:contents}
  .table-row{display:contents}
  .first-row-cell{padding-top:14px;border-top:none}
  .size-label{
    font-family:"Poppins",Arial,sans-serif;font-weight:800;font-size:37px;color:#000;
  }
  .table-header{position:absolute;left:0;top:0;width:1018px;height:128px}
  .header-label{
    position:absolute;top:20px;height:60px;display:flex;align-items:center;justify-content:center;
    font-family:"Poppins",Arial,sans-serif;font-weight:700;font-size:40px;color:var(--white);
  }
  .notes{position:absolute;left:81px;top:805px}
  .notes-title{font-weight:600;font-size:30px;line-height:42px;color:var(--text)}
  .notes-list{list-style:none;margin-top:18px}
  .notes-list li{
    position:relative;padding-left:38px;font-size:22.5px;line-height:36.5px;color:var(--text);
  }
  .notes-list li::before{
    content:"";position:absolute;left:5px;top:13px;width:11px;height:11px;border-radius:50%;background:#000;
  }
</style>
</head>
<body>
  <div class="title-rule left"></div>
  <div class="title-rule right"></div>
  <h1 class="chart-title">Size Chart</h1>
  <p class="chart-unit">Size Chart (Unit:- cm/inch)</p>

  <div class="size-table">
    <div class="cell header-cell"></div>
    <div class="cell header-cell"></div>
    <div class="cell header-cell"></div>
    <div class="cell header-cell"></div>

    <div class="cell first-row-cell"><span class="size-label">S</span></div>
    <div class="cell first-row-cell">90cm/35.4”</div>
    <div class="cell first-row-cell">98cm/38.6”</div>
    <div class="cell first-row-cell">81cm/31.5”</div>

    <div class="cell"><span class="size-label">M</span></div>
    <div class="cell">94cm/37”</div>
    <div class="cell">102cm/40.2”</div>
    <div class="cell">81cm/31.9”</div>

    <div class="cell"><span class="size-label">L</span></div>
    <div class="cell">98cm/38.6”</div>
    <div class="cell">106cm/41.7”</div>
    <div class="cell">82cm/32.3”</div>

    <div class="cell"><span class="size-label">XL</span></div>
    <div class="cell">102cm/40.2”</div>
    <div class="cell">110cm/43.3”</div>
    <div class="cell">83cm/33.7”</div>

    <div class="cell"><span class="size-label">2XL</span></div>
    <div class="cell">106cm/41.7”</div>
    <div class="cell">114cm/44.9”</div>
    <div class="cell">84cm/33.1”</div>

    <svg class="table-header" viewBox="0 0 1018 128" aria-hidden="true">
      <polygon points="0,0 256,0 256,101 128,128 0,101" fill="var(--size-pink)"/>
      <polygon points="256,0 511,0 511,101 383,128 256,101" fill="var(--bust-purple)"/>
      <polygon points="511,0 765,0 765,101 638,128 511,101" fill="var(--waist-amber)"/>
      <polygon points="765,0 1018,0 1018,101 892,128 765,101" fill="var(--length-blue)"/>
    </svg>
    <div class="header-label" style="left:0;width:256px">Size</div>
    <div class="header-label" style="left:256px;width:255px">Bust</div>
    <div class="header-label" style="left:511px;width:254px">Waist</div>
    <div class="header-label" style="left:765px;width:253px">Length</div>
  </div>

  <section class="notes">
    <h2 class="notes-title">Important Notes :-</h2>
    <ul class="notes-list">
      <li>Please allow 1-2 cm measuring deviation due to manual measurement.</li>
      <li>Please check the size chart before order.</li>
      <li>If you are not sure the size, please send message to us.</li>
    </ul>
  </section>
</body>
</html>
```